50 plus

Full Color 1/8 page newspaper ad . We are 1 stop shop for all mobility needs. Highlight Accessible Van Rentals & Sales. 50 free miles on your rental when you mention this ad.

```html
<!DOCTYPE html>
<html lang="en">
<head>
<meta charset="utf-8">
<title>Summit Access &amp; Mobility – Newspaper Ad</title>
<link rel="stylesheet" href="https://fonts.googleapis.com/css2?family=Bebas+Neue&family=Pathway+Gothic+One&family=Nunito:wght@700;800&family=Varela+Round&display=swap">
<style>
  :root {
    --navy: #271c5e;
    --ink: #272064;
    --white: #ffffff;
    --sign-ink: #1b1b1b;
    --silver-light: #d3d4da;
    --silver-mid: #a9aab3;
    --silver-dark: #6f707c;
    --chair-tone: #2c2f3d;
    --scooter-tone: #9e1b2e;
    --knee-tone: #55565e;
    --rollator-tone: #4a5391;
    --web-blue: #3cc6f0;
    --video-red: #e8191c;
    --social-blue: #1877f2;
  }
  * { margin: 0; padding: 0; box-sizing: border-box; }
  html, body { width: 1189px; height: 1200px; overflow: hidden; }
  body { background: var(--white); font-family: "Bebas Neue", sans-serif; }

  .ad { position: relative; width: 1189px; height: 1200px; }

  .hero {
    position: absolute; left: 0; top: 0; width: 1189px; height: 1034px;
    background: var(--navy); color: var(--white);
  }

  .headline { position: absolute; left: 62px; top: 86px; line-height: 1; font-weight: 400; }
  .headline-top { display: flex; align-items: baseline; gap: 30px; white-space: nowrap; }
  .headline-your { font-size: 100px; }
  .headline-big { font-size: 152px; letter-spacing: 1px; }
  .headline-bottom { font-size: 103px; margin-top: -6px; letter-spacing: 0.5px; white-space: nowrap; }

  .van-photo {
    position: absolute; left: 50px; top: 362px; width: 860px; height: 430px;
    border-radius: 70px 180px 40px 60px;
    background: linear-gradient(170deg, var(--silver-light) 0%, var(--silver-mid) 55%, var(--silver-dark) 100%);
  }

  .product-photo { position: absolute; left: 922px; width: 208px; height: 208px; }
  .product-photo.chair    { top: 100px; background: radial-gradient(circle at 52% 50%, var(--chair-tone) 0%, #8a8c98 38%, var(--white) 72%); }
  .product-photo.scooter  { top: 323px; background: radial-gradient(circle at 55% 55%, var(--scooter-tone) 0%, #c9808a 38%, var(--white) 72%); }
  .product-photo.knee     { top: 544px; width: 211px; height: 211px; background: radial-gradient(circle at 50% 55%, var(--knee-tone) 0%, #a3a4aa 38%, var(--white) 72%); }
  .product-photo.rollator { top: 770px; width: 210px; background: radial-gradient(circle at 50% 52%, var(--rollator-tone) 0%, #9ea4c9 38%, var(--white) 72%); }

  .body-copy {
    position: absolute; left: 46px; top: 808px;
    font-family: "Pathway Gothic One", sans-serif; font-size: 31px; line-height: 33px;
    letter-spacing: 0.6px; white-space: nowrap;
  }

  .mile-sign {
    position: absolute; left: 554px; top: 817px; width: 119px; height: 157px;
    background: var(--white); border-radius: 8px; padding: 4px;
  }
  .mile-sign-inner {
    width: 100%; height: 100%; border: 3px solid var(--sign-ink); border-radius: 6px;
    color: var(--sign-ink); text-align: center;
    font-family: "Varela Round", sans-serif;
  }
  .mile-sign-word { font-size: 27px; line-height: 31px; }
  .mile-sign-word:first-child { margin-top: 8px; }
  .mile-sign-number { font-size: 58px; line-height: 62px; }

  .promo {
    position: absolute; left: 688px; top: 829px;
    font-size: 32px; line-height: 32.5px; white-space: nowrap;
  }

  .footer { position: absolute; left: 0; top: 1034px; width: 1189px; height: 166px; }

  .brand {
    position: absolute; left: 38px; top: 30px; width: 355px; height: 110px;
    background: var(--navy); display: flex; align-items: center; justify-content: center; gap: 12px;
    color: var(--white); font-size: 32px; letter-spacing: 1px; white-space: nowrap;
  }
  .brand-mark { width: 16px; height: 16px; background: var(--white); flex: none; }

  .phones {
    position: absolute; right: 315px; top: 54px; text-align: right;
    color: var(--ink); font-size: 47px; line-height: 40px; white-space: nowrap;
  }

  .handle {
    position: absolute; left: 916px; top: 36px;
    color: var(--ink); font-family: "Nunito", sans-serif; font-weight: 800; font-size: 29px; letter-spacing: 1.5px;
  }

  .social { position: absolute; left: 909px; top: 82px; display: flex; gap: 24px; }
  .social-dot { width: 55px; height: 55px; border-radius: 50%; }
  .social-dot.video { background: var(--video-red); }
  .social-dot.network { background: var(--social-blue); }
</style>
</head>
<body>
<div class="ad">
  <section class="hero">
    <h1 class="headline">
      <div class="headline-top"><span class="headline-your">Your</span><span class="headline-big">1-Stop Shop</span></div>
      <div class="headline-bottom">For All Mobility Needs</div>
    </h1>

    <div class="van-photo" role="img" aria-label="Silver wheelchair-accessible minivan with side ramp deployed and a man in a power wheelchair"></div>

    <div class="product-photo chair" role="img" aria-label="Power wheelchair"></div>
    <div class="product-photo scooter" role="img" aria-label="Red mobility scooter"></div>
    <div class="product-photo knee" role="img" aria-label="Knee walker"></div>
    <div class="product-photo rollator" role="img" aria-label="Rollator walker with seat"></div>

    <p class="body-copy">Lorem ipsum dolor sit amet, consectetur<br>adipiscing elit.&nbsp; Morbi ultricies molestie<br>rci.&nbsp; Aenean purus mauris, sodales nec<br>diam dignissim, porttitor laoreet enim. A<br>liquam id sollicitudin turpis.</p>

    <div class="mile-sign">
      <div class="mile-sign-inner">
        <div class="mile-sign-word">FREE</div>
        <div class="mile-sign-word">MILES</div>
        <div class="mile-sign-number">50</div>
      </div>
    </div>

    <p class="promo">50 Free Miles<br>On Your Rental<br>When You Mention<br>This Ad</p>
  </section>

  <footer class="footer">
    <div class="brand"><span class="brand-mark"></span><span>Summit Access &amp; Mobility</span></div>

    <div class="phones">
      <div>Fort Collins (970) 555.0142</div>
      <div>Cheyenne (307) 555.0188</div>
    </div>

    <div class="handle">summitaccess</div>

    <div class="social">
      <svg class="social-dot" viewBox="0 0 56 56" role="img" aria-label="Website">
        <g fill="none" stroke="var(--web-blue)" stroke-width="3.5">
          <circle cx="28" cy="28" r="25"/>
          <ellipse cx="28" cy="28" rx="11" ry="25"/>
          <line x1="3" y1="28" x2="53" y2="28"/>
          <line x1="28" y1="3" x2="28" y2="53"/>
        </g>
      </svg>
      <div class="social-dot video" role="img" aria-label="Video channel"></div>
      <div class="social-dot network" role="img" aria-label="Social page"></div>
    </div>
  </footer>
</div>
</body>
</html>
```